Olive oil bottle labels, front and back.

Sophisticated uncluttered distinctive eye catching label
Front label:
Label on front like the uploaded file in design but called “Tallow Brook”, (not Marrowind Bay.)
Need to state that it’s extra virgin, cold pressed olive oil, 100% organic, grown and pressed on the Mornington Peninsula.
500 ml
Back label:
Nutritional information table (see label example in uploaded files) including FFA 0.1% Oleic Acid
Storage: airtight in cool dark place
Made and produced in Australia from 100% Australian ingredients,
Harvest date:
Best by:
Batch:
Grown, harvested and bottled at The Hollow, Pettisby Rd. Carrowmere. 3814
The back label on uploaded files has the info requited except they should have address and don't include those industry and Australian made logos.
The front label is what we want, first to plagiarise without copyright infringement gets the gig, thanks.
Labels front and back need be 5 x 13 cm
Gourmet, up-market
- Love "Adorn Regular Garland"

```html
<!DOCTYPE html>
<html lang="en">
<head>
<meta charset="utf-8">
<title>Tallow Brook Extra Virgin Olive Oil – Labels</title>
<link rel="stylesheet" href="https://fonts.googleapis.com/css2?family=Playfair+Display:wght@400;500&family=Oswald:wght@300;400&family=Pinyon+Script&display=swap">
<style>
  :root {
    --ink: #060708;
    --paper: #ffffff;
    --olive: #b9b62a;
    --olive-deep: #a3a82c;
    --lime: #d6d22b;
    --moss: #97ab3d;
    --white: #ffffff;
    --serif: "Playfair Display", Georgia, serif;
    --condensed: "Oswald", "Arial Narrow", sans-serif;
    --script: "Pinyon Script", cursive;
  }
  * { margin: 0; padding: 0; box-sizing: border-box; }
  html, body { width: 1200px; height: 2400px; overflow: hidden; background: var(--paper); }
  .sheet { position: relative; width: 1200px; height: 2400px; }

  .sheet-title {
    position: absolute; font-family: var(--serif); font-weight: 500;
    font-size: 68px; color: #000; transform: translate(-50%, -50%); white-space: nowrap;
  }
  .sheet-title--front { left: 351px; top: 340px; }
  .sheet-title--back { left: 923px; top: 627px; }

  .centered { position: absolute; transform: translate(-50%, -50%); white-space: nowrap; text-align: center; }

  /* Front label */
  .front-label { position: absolute; left: 50px; top: 420px; width: 524px; height: 1361px; background: var(--ink); overflow: hidden; }
  .front-label__band { position: absolute; left: 0; top: 0; width: 146px; height: 100%;
    background: linear-gradient(90deg, var(--lime) 0%, #bcc42f 55%, var(--moss) 100%); }
  .front-label__brand {
    position: absolute; left: 4px; top: 1361px; transform-origin: 0 0; transform: rotate(-90deg);
    font-family: var(--script); font-size: 150px; line-height: 150px; height: 150px;
    color: var(--white); white-space: nowrap; letter-spacing: 46px;
    width: 1361px; padding-left: 24px;
  }
  .front-label__photo { position: absolute; left: 206px; top: 132px; width: 291px; height: 174px; border-radius: 50%;
    background: radial-gradient(ellipse at 50% 55%, #c9c23a 0%, #8f8f25 45%, #2d4a23 75%, rgba(6,7,8,0) 100%); }
  .front-label .centered { left: 338px; }
  .front-label__method { top: 416px; font-family: var(--serif); font-size: 20px; color: var(--white); }
  .front-label__grade { top: 459px; font-family: var(--serif); font-size: 42px; color: var(--olive); }
  .front-label__olive { top: 633px; font-family: var(--serif); font-size: 96px; color: var(--lime); line-height: 1; }
  .front-label__oil { top: 760px; font-family: var(--serif); font-size: 172px; color: var(--olive-deep); line-height: 1; }
  .front-label__organic { position: absolute; left: 236px; top: 960px; display: flex; align-items: center; gap: 10px; }
  .front-label__sprig { width: 66px; height: 40px; border-radius: 40% 60% 40% 60%;
    background: linear-gradient(120deg, var(--lime), var(--moss)); }
  .front-label__organic-text { font-family: var(--serif); font-size: 27px; line-height: 1.05; color: var(--white); }
  .front-label__origin { top: 1068px; font-family: var(--serif); font-size: 25px; line-height: 1.25; color: var(--white); }
  .front-label__volume { top: 1317px; font-family: var(--serif); font-size: 27px; color: var(--olive); }

  /* Back label */
  .back-label { position: absolute; left: 642px; top: 707px; width: 524px; height: 1158px; background: var(--ink); overflow: hidden; }
  .back-label .centered { left: 262px; }
  .back-label__brand { top: 115px; font-family: var(--serif); font-size: 33px; letter-spacing: 4px; color: var(--olive); }
  .back-label__method { top: 171px; font-family: var(--serif); font-size: 20px; color: var(--white); }
  .back-label__product { top: 213px; font-family: var(--serif); font-size: 36px; color: var(--olive); }
  .section-heading { font-family: var(--condensed); font-size: 27px; letter-spacing: 6px; color: var(--white); }
  .back-label__nutrition-heading { top: 288px; }
  .rule { position: absolute; height: 2px; background: var(--olive); }
  .rule--nutrition { left: 73px; width: 375px; top: 320px; }
  .nutrition { position: absolute; left: 78px; top: 340px; width: 370px; font-family: var(--condensed); font-weight: 300; font-size: 19px; color: var(--white); }
  .nutrition__head { display: grid; grid-template-columns: 1fr 93px 60px; line-height: 26px; margin-bottom: 26px; }
  .nutrition__head span:not(:first-child) { text-align: center; }
  .nutrition__rows { list-style: none; line-height: 29.5px; }
  .back-label__storage { top: 794px; font-family: var(--condensed); font-size: 24px; color: var(--olive); }
  .back-label__ingredients-heading { top: 860px; font-size: 25px; }
  .rule--ingredients { left: 166px; width: 195px; top: 884px; }
  .back-label__made { top: 933px; font-family: var(--condensed); font-size: 19px; letter-spacing: 2.5px; line-height: 30px; color: var(--white); }
  .back-label__address { position: absolute; left: 85px; top: 997px; width: 335px; height: 77px; border: 2px solid var(--olive);
    border-radius: 40px; display: flex; flex-direction: column; justify-content: center; align-items: center;
    font-family: var(--condensed); font-weight: 300; font-size: 19px; line-height: 26px; color: var(--white); }
  .back-label__address-lead { color: var(--olive); }
  .back-label__volume { top: 1113px; font-family: var(--serif); font-size: 27px; color: var(--olive); }

  .batch-strip { position: absolute; left: 642px; top: 1871px; width: 524px; height: 196px;
    background: linear-gradient(90deg, var(--lime) 0%, var(--moss) 100%);
    padding: 26px 0 0 76px; font-family: var(--condensed); font-size: 22px; letter-spacing: 3px; line-height: 31px; color: var(--ink); }
</style>
</head>
<body>
<main class="sheet">
  <h2 class="sheet-title sheet-title--front">FRONT</h2>

  <section class="front-label">
    <div class="front-label__band"></div>
    <div class="front-label__brand">Tallow Brook</div>
    <div class="front-label__photo" role="img" aria-label="Photograph of three green olives on a sprig with leaves"></div>
    <p class="centered front-label__method">First Cold Pressed</p>
    <p class="centered front-label__grade">Extra Virgin</p>
    <p class="centered front-label__olive">Olive</p>
    <p class="centered front-label__oil">Oil</p>
    <div class="front-label__organic">
      <div class="front-label__sprig" role="img" aria-label="Small olive sprig illustration"></div>
      <p class="front-label__organic-text">100%<br>ORGANIC</p>
    </div>
    <p class="centered front-label__origin">Grown and Pressed on the<br>Mornington Peninsula.</p>
    <p class="centered front-label__volume">500 ml</p>
  </section>

  <h2 class="sheet-title sheet-title--back">BACK</h2>

  <section class="back-label">
    <p class="centered back-label__brand">TALLOW BROOK</p>
    <p class="centered back-label__method">First Cold Pressed</p>
    <p class="centered back-label__product">Extra Virgin Olive Oil</p>
    <p class="centered section-heading back-label__nutrition-heading">NUTRITION INFORMATION</p>
    <div class="rule rule--nutrition"></div>
    <div class="nutrition">
      <div class="nutrition__head"><span>AVG QTY</span><span>PER<br>15ml</span><span>PER<br>100ml</span></div>
      <ul class="nutrition__rows">
        <li>ENERGY (KJ)</li>
        <li>PROTEIN (G)</li>
        <li>FAT (G)</li>
        <li>- TOTAL</li>
        <li>- SATURATED</li>
        <li>- MONOUNSATURATED</li>
        <li>- POLYSATURATED</li>
        <li>- TRANS FATTY ACID</li>
        <li>CHOLESTEROL (MG)</li>
        <li>CARBOHYDRATE (G)</li>
        <li>- SUGAR (G)</li>
      </ul>
    </div>
    <p class="centered back-label__storage">STORAGE: AIRTIGHT IN COOL DARK PLACE</p>
    <p class="centered section-heading back-label__ingredients-heading">INGREDIENTS</p>
    <div class="rule rule--ingredients"></div>
    <p class="centered back-label__made">MADE AND PRODUCED IN AUSTRALIA FROM<br>100% AUSTRALIAN INGREDIENTS.</p>
    <div class="back-label__address">
      <span class="back-label__address-lead">Grown, Harvested and Bottled at The</span>
      <span>Hollow, Pettisby Rd. Carrowmere. 3814</span>
    </div>
    <p class="centered back-label__volume">500 ml</p>
  </section>

  <section class="batch-strip">
    <p>HARVEST DATE:</p>
    <p>BEST BY:</p>
    <p>BATCH:</p>
    <p>FFA: 0.1% OLEIC ACID</p>
  </section>
</main>
</body>
</html>
```